Buiilding & Construction WebSite

Build a website for the domain www.talbrookhg.com.au
Talbrook Housing Group Pty Ltd of Australia

Please review the docx file I have attached, It shows the web sites I like.
Pls ignore the Designers and Freight Forwarders Sections.

Target Market(s)

Consumers building houses, renovating or upgrading. People building pools, people wanting new kitchens

Industry/Entity Type

Residential Construction

Coding

Coded - Design and coding required

Number of Pages Required

5+ page

Colors

Designer to choose colors to be used in the design.

Requirements
Must have
• Uniqueness
Should not have
• Old styling

```html
<!DOCTYPE html>
<html lang="en">
<head>
<meta charset="utf-8">
<title>Talbrook Housing Group Pty Ltd</title>
<link rel="stylesheet" href="https://fonts.googleapis.com/css2?family=Ubuntu:ital,wght@0,300;0,400;0,500;0,700;1,300;1,400&display=swap">
<style>
:root{
  --blue:#1f5597;
  --blue-deep:#0f3a73;
  --blue-band:#144a8c;
  --heading-blue:#1d5499;
  --ink:#333;
  --white:#fff;
  --grey-logo:#b9b9b9;
  --footer:#2a2a2a;
  --footer-bottom:#161616;
  --red:#e8333a;
  --caption:rgba(20,20,20,.72);
}
*{box-sizing:border-box;margin:0;padding:0}
html,body{width:1200px;height:2532px;overflow:hidden}
body{font-family:'Ubuntu',sans-serif;color:var(--ink);background:var(--white);position:relative}
.abs{position:absolute}

/* hero */
.hero{position:absolute;left:0;top:0;width:1200px;height:587px;
  background:linear-gradient(180deg,#5a6e86 0%,#7d8b99 30%,#8f8a7d 60%,#5d5346 85%,#3b4a66 100%)}
.topbar{position:absolute;top:10px;right:25px;display:flex;align-items:center;gap:14px;color:var(--white);font-size:14px}
.topbar .phone{display:flex;align-items:center;gap:8px;margin-right:22px}
.social{width:24px;height:24px;border-radius:50%;background:#e6e6e6}
.brand{position:absolute;left:25px;top:64px;color:var(--white);font-size:34px;font-weight:500;line-height:1.05;width:300px}
.nav{position:absolute;top:88px;right:25px;display:flex;gap:37px;font-size:13.5px;color:var(--white);text-transform:uppercase}
.nav .active{position:relative}
.nav .active::after{content:"";position:absolute;left:0;right:0;bottom:-9px;height:2px;background:var(--white)}
.hero-kicker{position:absolute;left:121px;top:212px;color:var(--white);font-size:25px;font-weight:700}
.hero-title{position:absolute;left:118px;top:236px;color:var(--white);font-weight:300;line-height:1}
.hero-title .l1{font-size:62px;display:block}
.hero-title .l2{font-size:140px;display:block;margin-top:-6px;letter-spacing:1px}
.btn{display:inline-flex;align-items:center;justify-content:center;font-size:16px;text-transform:uppercase}
.btn-light{background:linear-gradient(#fafafa,#cfd3d8);color:var(--blue-deep)}
.btn-blue{background:var(--blue);color:var(--white)}
.hero .b1{position:absolute;left:127px;top:446px;width:155px;height:35px}
.hero .b2{position:absolute;left:322px;top:446px;width:156px;height:35px}
.arrow-side{position:absolute;top:275px;color:rgba(255,255,255,.8);font-size:42px;font-weight:300}
.notch{position:absolute;left:0;top:498px}
.dots{position:absolute;top:562px;left:563px;display:flex;gap:9px}
.dots span{width:11px;height:11px;border-radius:50%;background:rgba(255,255,255,.55)}
.dots span:first-child{background:var(--white)}

/* call band */
.band{position:absolute;left:0;top:587px;width:1200px;height:125px;background:linear-gradient(90deg,var(--blue-deep),var(--blue-band) 50%,var(--blue-deep))}
.band p{position:absolute;left:120px;top:44px;color:var(--white);font-size:31px;font-weight:300}
.band .btn{position:absolute;left:910px;top:44px;width:166px;height:40px}

/* services */
.sec-title{position:absolute;left:0;width:1200px;text-align:center;color:var(--heading-blue);font-size:33px;font-weight:700;text-transform:uppercase}
.services-sub{position:absolute;left:0;top:788px;width:1200px;text-align:center;font-size:15.5px;color:#222;text-transform:uppercase}
.card{position:absolute;width:562px;height:393px;overflow:hidden}
.card .photo{position:absolute;inset:0}
.card .cap{position:absolute;left:0;right:0;bottom:0;height:107px;background:var(--caption);color:var(--white);padding:14px 18px}
.card h3{font-size:20px;font-weight:400;margin-bottom:6px}
.card p{font-size:11.5px;line-height:1.3;width:360px;color:#e8e8e8}
.card .more{position:absolute;right:16px;bottom:16px;width:101px;height:26px;font-size:11.5px;background:linear-gradient(#fff,#d6d6d6);color:#333}

/* testimonials */
.testi{position:absolute;left:0;top:1671px;width:1200px;height:392px;background:linear-gradient(180deg,#3a6ba8 0%,#2e5f9f 55%,#345f94 100%)}
.testi .sec-title{top:24px;color:var(--white);font-size:31px}
.testi .pager{position:absolute;top:69px;left:1114px;display:flex;gap:4px}
.testi .pager span{width:29px;height:31px;display:flex;align-items:center;justify-content:center;color:var(--white);font-size:20px;font-weight:700}
.testi .pager .on{background:var(--white);color:var(--blue)}
.avatar{position:absolute;left:27px;top:149px;width:168px;height:168px;border-radius:50%;border:4px solid var(--white);background:radial-gradient(circle at 50% 40%,#a57e60,#4b5768 75%)}
.quote{position:absolute;left:215px;top:168px;width:955px;text-align:center;color:var(--white);font-size:20px;font-style:italic;font-weight:300;line-height:1.27}
.author{position:absolute;right:27px;top:240px;color:var(--white);font-size:20px}

/* partners */
.partners{position:absolute;left:0;top:2168px;width:1200px;display:flex;justify-content:space-between;align-items:center;padding:0 25px}
.partner{color:var(--grey-logo);font-size:46px;font-weight:700;display:flex;align-items:center;gap:12px}
.partner .mark{width:46px;height:46px;background:var(--grey-logo)}

/* footer */
.footer{position:absolute;left:0;top:2291px;width:1200px;height:211px;background:linear-gradient(180deg,#2e2e2e,var(--footer))}
.fcol{position:absolute;top:34px;color:var(--white);font-size:11.5px;text-transform:uppercase}
.fcol h4{font-size:14px;font-weight:400;margin-bottom:19px}
.fcol li{list-style:none;height:25px}
.fcol .addr{text-transform:none;font-size:12px;line-height:1.4}
.fcol .ci{display:flex;align-items:center;gap:12px;text-transform:none;font-size:12px;margin-top:10px}
.subscribe{display:flex;margin-top:18px}
.subscribe span{width:168px;height:32px;background:var(--white)}
.subscribe b{width:100px;height:32px;background:var(--red);color:var(--white);font-weight:400;display:flex;align-items:center;justify-content:center;font-size:12.5px}
.bottom{position:absolute;left:0;top:2502px;width:1200px;height:30px;background:var(--footer-bottom);color:#ddd;font-size:11.5px;display:flex;align-items:center;justify-content:space-between;padding:0 25px}
.bottom .icons{display:flex;gap:16px}
.bottom .icons span{width:18px;height:18px;border-radius:50%;background:#cfcfcf}
</style>
</head>
<body>

<header class="hero">
  <div class="hero-bg abs" role="img" aria-label="Large two-storey white colonial house with verandas and a pool terrace at dusk" style="inset:0"></div>
  <div class="topbar">
    <span class="phone">
      <svg width="16" height="16" viewBox="0 0 16 16"><path d="M4 2 L6 5 L5 6.5 C6 8.5 7.5 10 9.5 11 L11 10 L14 12 L12.5 14.5 C7 14 2 9 1.5 3.5 Z" fill="none" stroke="#fff" stroke-width="1.4"/></svg>
      61 (07) 4000 1186
    </span>
    <span class="social"></span><span class="social"></span><span class="social"></span><span class="social"></span>
  </div>
  <div class="brand">Talbrook Housing Group Pty Ltd</div>
  <nav class="nav">
    <span class="active">Home</span><span>About Us</span><span>Building Houses</span><span>Renovation</span><span>Building Pools</span><span>New Kitchens</span><span>Contact Us</span>
  </nav>
  <span class="arrow-side" style="left:22px">&#10216;</span>
  <span class="arrow-side" style="right:14px">&#10217;</span>
  <div class="hero-kicker">Houses</div>
  <h1 class="hero-title"><span class="l1">As Grand as your</span><span class="l2">DREAMS</span></h1>
  <span class="btn btn-light b1">Know More</span>
  <span class="btn btn-blue b2">Get a Quote</span>
  <svg class="notch" width="1200" height="90" viewBox="0 0 1200 90"><polygon points="517,89 600,0 683,89" fill="#2a5c9a" opacity=".92"/></svg>
  <div class="dots"><span></span><span></span><span></span><span></span></div>
</header>

<section class="band">
  <p>Let us mesmerize you with our salient services</p>
  <span class="btn btn-light">Get a Quote</span>
</section>

<h2 class="sec-title" style="top:728px">Services We Are Offering</h2>
<p class="services-sub">Consumers Building Houses &nbsp;|&nbsp; Renovating or Upgrading &nbsp;|&nbsp; People Building Pools &nbsp;|&nbsp; People Wanting New Kitchens</p>

<article class="card" style="left:25px;top:832px">
  <div class="photo" role="img" aria-label="Red-roofed Victorian house under a blue sky" style="background:linear-gradient(180deg,#3f8ad6 0%,#8bb8e0 35%,#8a4a35 55%,#3b4a3a 100%)"></div>
  <div class="cap"><h3>Building Houses</h3><p>Duis vitae rutrum ipsum. Morbi aliquet convallis arcu sit amet consequat. Curabitur suscipit interdum ante, eu euismod nisi bibendum a. Curabitur vel venenatis nisl.</p><span class="btn more">Know More</span></div>
</article>
<article class="card" style="left:613px;top:832px">
  <div class="photo" role="img" aria-label="Paint roller, brushes and tray on a windowsill" style="background:linear-gradient(180deg,#d9d7d0 0%,#cfc8b8 40%,#6b5f55 75%,#3a3430 100%)"></div>
  <div class="cap"><h3>Renovating or Upgrading</h3><p>Duis vitae rutrum ipsum. Morbi aliquet convallis arcu sit amet consequat. Curabitur suscipit interdum ante, eu euismod nisi bibendum a. Curabitur vel venenatis nisl.</p><span class="btn more">Know More</span></div>
</article>
<article class="card" style="left:25px;top:1251px">
  <div class="photo" role="img" aria-label="Backyard swimming pool with red lounge chairs and trees" style="background:linear-gradient(180deg,#9cbf86 0%,#5f8a4a 35%,#3aa4d8 60%,#8b2a2a 85%,#3a2a2a 100%)"></div>
  <div class="cap"><h3>Building Pools</h3><p>Duis vitae rutrum ipsum. Morbi aliquet convallis arcu sit amet consequat. Curabitur suscipit interdum ante, eu euismod nisi bibendum a. Curabitur vel venenatis nisl.</p><span class="btn more">Know More</span></div>
</article>
<article class="card" style="left:613px;top:1251px">
  <div class="photo" role="img" aria-label="Bright modern kitchen with white cabinets and stove" style="background:linear-gradient(180deg,#e6e0d6 0%,#d8cfc2 45%,#b8a894 75%,#6f6456 100%)"></div>
  <div class="cap"><h3>New Kitchens</h3><p>Duis vitae rutrum ipsum. Morbi aliquet convallis arcu sit amet consequat. Curabitur suscipit interdum ante, eu euismod nisi bibendum a. Curabitur vel venenatis nisl.</p><span class="btn more">Know More</span></div>
</article>

<section class="testi" role="img" aria-label="City skyline and harbour tinted blue">
  <h2 class="sec-title">Testimonials</h2>
  <div class="pager"><span>&laquo;</span><span class="on">&raquo;</span></div>
  <div class="avatar" role="img" aria-label="Portrait of client"></div>
  <p class="quote">“ Nullam convallis gravida iaculis. Maecenas bibendum nulla at enim pulvinar gravida. Cras ac tempus tellus. Aliquam nunc lorem, placerat eget molestie id, tristique in neque. Etiam sed tellus eu quam laoreet mattis vel sed purus. Vivamus at urna vel tellus scelerisque semper. ”</p>
  <p class="author">— Marcus Ellery</p>
</section>

<h2 class="sec-title" style="top:2084px">Our Patrons and Partners</h2>
<div class="partners">
  <span class="partner"><span class="mark"></span>NORVEX</span>
  <span class="partner" style="font-size:36px">Stoneway Supply</span>
  <span class="partner" style="font-size:36px">HARLOWE</span>
  <span class="partner">LUMORA</span>
</div>

<footer class="footer">
  <div class="fcol" style="left:25px"><h4>Quick Links</h4><ul><li>Home</li><li>Building Houses</li><li>Renovations</li><li>Building Pools</li><li>New Kitchens</li></ul></div>
  <div class="fcol" style="left:319px"><h4>More Links</h4><ul><li>Privacy Policy</li><li>Terms &amp; Conditions</li><li>Contact Us</li></ul></div>
  <div class="fcol" style="left:613px"><h4>Be Informed About Us</h4><ul><li>About Us</li><li>Newsletter Submission</li></ul>
    <div class="subscribe"><span></span><b>SUBSCRIBE</b></div></div>
  <div class="fcol" style="left:906px"><h4>Get in Touch With Us</h4>
    <p class="addr">Office Address:<br>14 Wattlebrook Lane<br>HILLVALE QLD 4390</p>
    <p class="ci"><svg width="16" height="16" viewBox="0 0 16 16"><path d="M4 2 L6 5 L5 6.5 C6 8.5 7.5 10 9.5 11 L11 10 L14 12 L12.5 14.5 C7 14 2 9 1.5 3.5 Z" fill="none" stroke="#fff" stroke-width="1.4"/></svg>61 (07) 4000 2297</p>
    <p class="ci"><svg width="18" height="13" viewBox="0 0 18 13"><rect x="1" y="1" width="16" height="11" fill="none" stroke="#fff" stroke-width="1.3"/><path d="M1 1 L9 7 L17 1" fill="none" stroke="#fff" stroke-width="1.3"/></svg>info@talbrookhg.com.au</p>
  </div>
</footer>
<div class="bottom"><span>© 2017 www.talbrookhg.com.au</span><span class="icons"><span></span><span></span><span></span><span></span></span></div>

</body>
</html>
```